Propose a revamped landing page

One template we like eg is https://www.trovask.com but but cluttered Our logo and colors are attached to our logo and colors are printed on a white background what we have. So font usage ...
1 page

```html
<!DOCTYPE html>
<html lang="en">
<head>
<meta charset="utf-8">
<title>Voltara – Always switch to the cheapest energy provider</title>
<link href="https://fonts.googleapis.com/css2?family=Montserrat:wght@400;500;600;700;800&display=swap" rel="stylesheet">
<style>
:root{
  --orange:#f39a1e;
  --orange-deep:#e8850f;
  --orange-soft:#fbc36a;
  --ink:#2f3740;
  --text:#55606b;
  --muted:#8a949e;
  --white:#ffffff;
  --paper:#fbfbfb;
  --navy:#363e47;
  --sky:#2f8fb3;
  --teal:#2fb3a6;
}
*{margin:0;padding:0;box-sizing:border-box}
html,body{width:1200px;height:2824px;overflow:hidden;background:var(--white)}
body{font-family:"Montserrat",sans-serif;color:var(--text);position:relative}
.abs{position:absolute}
svg.bg{position:absolute;left:0;top:0}

/* header */
.brand{left:64px;top:24px;font-weight:800;font-size:40px;line-height:1;color:var(--orange);display:flex;align-items:center;gap:10px}
.brand .dot{width:18px;height:18px;border-radius:50%;background:var(--orange)}
.nav{right:70px;top:26px;display:flex;gap:22px;align-items:center;font-size:10.5px;font-weight:700;letter-spacing:.5px;color:var(--ink)}
.nav .social{width:20px;height:20px;background:var(--sky);border-radius:3px}

/* hero */
.hero-title{left:64px;top:200px;width:520px;font-size:38px;font-weight:700;line-height:1.22;color:var(--ink)}
.btn{left:64px;top:360px;background:var(--orange-deep);color:#fff;font-size:12px;font-weight:700;letter-spacing:1px;padding:16px 34px;border-radius:30px}
.partners{left:64px;top:446px;display:flex;gap:26px;align-items:center}
.partners span{display:block;width:80px;height:16px;background:#c9ced3;border-radius:3px}
.hero-figure{left:740px;top:70px;width:330px;height:420px;border-radius:40% 40% 20% 20%;background:linear-gradient(180deg,#f5a93a,#e9821c)}

/* never pay */
.circle-illu{left:110px;top:960px;width:360px;height:360px;border-radius:50%;background:linear-gradient(180deg,#f7b04a 0%,#f39a1e 45%,#2fb3a6 46%,#1d8f86 100%)}
.never h2{left:600px;top:1010px;width:460px;font-size:32px;font-weight:700;line-height:1.25;color:var(--ink)}
.never p{font-size:12.5px;line-height:1.7;color:var(--text);width:440px}
.never .p1{left:600px;top:1112px}
.never .p2{left:600px;top:1160px}
.never .p3{left:600px;top:1232px}

/* prices */
.prices h2{left:110px;top:1360px;font-size:34px;font-weight:700;color:var(--ink);width:460px;line-height:1.2}
.prices h3{left:110px;top:1452px;font-size:22px;font-weight:500;color:var(--ink)}
.price-list{left:110px;top:1500px;list-style:none;width:540px}
.price-list li{display:flex;gap:12px;align-items:center;font-size:12.5px;line-height:1.4;margin-bottom:16px;color:var(--text)}
.price-list .tick{flex:none;width:20px;height:20px;border-radius:50%;border:2px solid var(--orange);display:flex;align-items:center;justify-content:center}
.footnote{left:110px;top:1680px;width:540px;font-size:9.5px;line-height:1.6;color:var(--muted)}
.city-illu{left:700px;top:1390px;width:400px;height:260px;border-radius:200px 200px 120px 120px;background:linear-gradient(180deg,#2f8fb3 0%,#2fb3a6 40%,#3b4550 41%,#2a3139 100%)}
.badge{left:840px;top:1310px;width:140px;height:140px;border-radius:50%;background:var(--orange);color:#fff;text-align:center;display:flex;flex-direction:column;justify-content:center}
.badge small{font-size:12px;font-weight:600;line-height:1.2}
.badge strong{font-size:30px;font-weight:800}

/* how */
.how-figure{left:150px;top:1760px;width:420px;height:760px;border-radius:46% 46% 10% 10%;background:linear-gradient(180deg,#f6a532,#e07f18)}
.how h2{left:600px;top:1950px;width:460px;font-size:34px;font-weight:600;line-height:1.25;color:#fff}
.step{left:600px;width:480px;display:flex;gap:24px;color:#fff}
.step .num{font-size:78px;font-weight:800;line-height:.9;color:var(--navy);width:48px}
.step h4{font-size:26px;font-weight:700;margin-bottom:4px}
.step p{font-size:12px;line-height:1.55;color:#fff4e4}
.s1{top:2080px}.s2{top:2200px}.s3{top:2320px}

/* register */
.register{left:0;top:2520px;width:1200px;height:248px;background:var(--navy)}
.register h2{position:absolute;top:40px;width:100%;text-align:center;font-size:30px;font-weight:500;color:var(--orange)}
.features{position:absolute;top:108px;left:150px;width:900px;display:flex;justify-content:space-between}
.feature{width:220px;text-align:center;color:#fff}
.feature svg{display:block;margin:0 auto 8px}
.feature h5{font-size:18px;font-weight:600;margin-bottom:6px}
.feature p{font-size:10.5px;line-height:1.5;color:#c6ccd2}
.footer{left:0;top:2768px;width:1200px;height:56px;display:flex;justify-content:center;align-items:center;gap:40px;font-size:10.5px;font-weight:700;letter-spacing:.5px;color:var(--ink)}
</style>
</head>
<body>

<svg class="bg" width="1200" height="2824" viewBox="0 0 1200 2824" aria-hidden="true">
  <!-- hero blob top right -->
  <path d="M640 0 H1200 V420 C1100 470 980 380 900 300 C820 220 700 180 640 0 Z" fill="#fdebd0"/>
  <!-- hero bottom wave -->
  <path d="M0 520 C250 470 520 560 800 520 C980 495 1100 440 1200 420 V470 C1080 520 960 560 780 580 C520 610 260 540 0 590 Z" fill="#f39a1e"/>
  <path d="M0 590 C260 540 520 610 780 580 C960 560 1080 520 1200 470 V500 C1080 560 940 600 760 620 C500 640 260 580 0 620 Z" fill="#fbc36a"/>
  <!-- section 3 background -->
  <path d="M0 860 C300 900 700 840 1200 880 V1780 C900 1820 400 1760 0 1800 Z" fill="#ffffff"/>
  <path d="M800 880 C950 860 1100 900 1200 840 V960 C1080 980 940 940 800 880 Z" fill="#f39a1e"/>
  <path d="M0 1260 C120 1230 200 1250 260 1300 C160 1300 80 1300 0 1320 Z" fill="#fbc36a"/>
  <!-- orange how section -->
  <path d="M0 1820 C300 1760 700 1840 1200 1740 V2520 H0 Z" fill="#f39a1e"/>
  <path d="M0 1860 C320 1800 720 1880 1200 1790 V1820 C720 1910 320 1830 0 1890 Z" fill="#f7ad45"/>
</svg>

<header>
  <div class="abs brand"><span>Voltara</span><span class="dot"></span></div>
  <nav class="abs nav">
    <span>HOW IT WORKS</span><span>PRICES</span><span>FAQ</span><span>ABOUT US</span><span>CONDITIONS</span><span>EXPERIENCE</span><span>BLOG</span><span class="social"></span>
  </nav>
</header>

<section class="hero">
  <h1 class="abs hero-title">Always automatically switch to the cheapest energy provider</h1>
  <a class="abs btn">REGISTER NOW</a>
  <div class="abs partners" aria-label="Press mentions"><span></span><span></span><span></span><span></span><span></span><span></span></div>
  <div class="abs hero-figure" role="img" aria-label="Illustrated superhero mascot in an orange suit and cape"></div>
</section>

<section class="never">
  <div class="abs circle-illu" role="img" aria-label="Round landscape illustration with a signpost pointing to hero"></div>
  <h2 class="abs">Never pay too much for electricity &amp; gas again</h2>
  <p class="abs p1">Gone are the days of bad deals, hidden fee surprises and boring contract hunts.</p>
  <p class="abs p2">With Voltara, your energy contract is checked every year and moved to a better offer when one appears. You sign up once, we do the rest.</p>
  <p class="abs p3">So ask your hero and start saving with Voltara today.</p>
</section>

<section class="prices">
  <h2 class="abs">The cheapest of all super powers</h2>
  <h3 class="abs">From 24 euros you are there:</h3>
  <ul class="abs price-list">
    <li><span class="tick"><svg width="10" height="10" viewBox="0 0 10 10"><path d="M1.5 5.5l2.2 2 4.8-5" stroke="#f39a1e" stroke-width="1.8" fill="none"/></svg></span>Service for electricity or gas (1 meter): 24 euros / year</li>
    <li><span class="tick"><svg width="10" height="10" viewBox="0 0 10 10"><path d="M1.5 5.5l2.2 2 4.8-5" stroke="#f39a1e" stroke-width="1.8" fill="none"/></svg></span>Service for electricity and gas (2 counters): 36 euros / year</li>
    <li><span class="tick"><svg width="10" height="10" viewBox="0 0 10 10"><path d="M1.5 5.5l2.2 2 4.8-5" stroke="#f39a1e" stroke-width="1.8" fill="none"/></svg></span>The first fee will be charged only after your first change</li>
    <li><span class="tick"><svg width="10" height="10" viewBox="0 0 10 10"><path d="M1.5 5.5l2.2 2 4.8-5" stroke="#f39a1e" stroke-width="1.8" fill="none"/></svg></span>Save up to 850 euros annually on electricity and gas costs at the first change*</li>
  </ul>
  <p class="abs footnote">*Savings figure based on an average household using 4,000 kWh electricity and 20,000 kWh gas per year compared with standard local tariffs. Actual savings depend on region and usage.</p>
  <div class="abs city-illu" role="img" aria-label="Night city skyline illustration in a rounded frame"></div>
  <div class="abs badge"><small>Savings<br>up to</small><strong>850,-</strong></div>
</section>

<section class="how">
  <div class="abs how-figure" role="img" aria-label="Illustrated superhero mascot standing with arms crossed"></div>
  <h2 class="abs">How do I become a Voltara member?</h2>
  <div class="abs step s1"><span class="num">1</span><div><h4>Once login</h4><p>Upload final bill statements. Select preferences. Finish the registration.</p></div></div>
  <div class="abs step s2"><span class="num">2</span><div><h4>Automatic</h4><p>Every year we find the cheapest tariff for you and switch the contract automatically.</p></div></div>
  <div class="abs step s3"><span class="num">3</span><div><h4>Sit back and save money</h4><p>We keep switching automatically to the best tariff.</p></div></div>
</section>

<section class="abs register">
  <h2>Register once, always save</h2>
  <div class="features">
    <div class="feature">
      <svg width="44" height="40" viewBox="0 0 44 40"><path d="M4 20 L40 4 L30 36 L20 24 Z" fill="none" stroke="#2fb3a6" stroke-width="3" stroke-linejoin="round"/><path d="M20 24 L40 4" stroke="#2fb3a6" stroke-width="3"/></svg>
      <h5>Independently</h5><p>We work only for you, free of any provider commissions.</p>
    </div>
    <div class="feature">
      <svg width="44" height="40" viewBox="0 0 44 40"><circle cx="16" cy="22" r="9" fill="none" stroke="#f39a1e" stroke-width="3"/><circle cx="32" cy="11" r="6" fill="none" stroke="#f39a1e" stroke-width="3"/></svg>
      <h5>automatically</h5><p>Your tariff is checked and switched without you lifting a finger.</p>
    </div>
    <div class="feature">
      <svg width="44" height="40" viewBox="0 0 44 40"><rect x="6" y="12" width="32" height="24" rx="3" fill="none" stroke="#e8850f" stroke-width="3"/><path d="M14 12 V6 H30 V12" fill="none" stroke="#e8850f" stroke-width="3"/></svg>
      <h5>fair</h5><p>Clear pricing, no hidden costs and cancel any time.</p>
    </div>
  </div>
</section>

<footer class="abs footer"><span>CONDITIONS</span><span>DATA PROTECTION</span><span>IMPRINT</span></footer>

</body>
</html>
```